Broschüre für Hersteller von Vendingautomaten
Zielgruppe
Unser Unternehmen ist ein Start-up im Bereich Vendingautomaten.
Wir stellen Verkaufsautomaten im öffentlichen Raum auf für Snacks, Getränke und Secret Packs.
Unsere Zielgruppe ist nicht genau zu definieren, aber primär Kinder bis Ende 50.
Aufgabenstellung
Bei dem Projekt geht es um eine Broschüre, um uns bei Kunden wie Privatpersonen aber auch Gemeinden und Städte, bekannt zu machen und uns zu präsentieren, damit diese wissen, mit wem sie es zu tun haben.

```html
<!DOCTYPE html>
<html lang="en">
<head>
<meta charset="utf-8">
<title>Vending Brochure – Inner Spread</title>
<link rel="stylesheet" href="https://fonts.googleapis.com/css2?family=Kaushan+Script&family=Poppins:wght@400;500&display=swap">
<style>
  :root {
    --backdrop: #e4e3e7;
    --page: #050505;
    --page-left: #161616;
    --ink: #ffffff;
    --machine-blue: #2c6fa8;
    --machine-green: #3f9a3a;
    --machine-red: #c0392b;
    --box-gold: #d9a94a;
    --glow: #fff1c4;
    --script: "Kaushan Script", cursive;
    --sans: "Poppins", sans-serif;
  }
  * { box-sizing: border-box; margin: 0; padding: 0; }
  html, body {
    width: 1200px;
    height: 850px;
    overflow: hidden;
    background: var(--backdrop);
  }
  .spread {
    position: absolute;
    left: 100px;
    top: 65px;
    width: 1000px;
    height: 720px;
    display: flex;
    box-shadow: 0 18px 40px rgba(0,0,0,0.25);
  }
  .page {
    position: relative;
    width: 500px;
    height: 720px;
    color: var(--ink);
    text-align: center;
  }
  .page--about {
    background: linear-gradient(90deg, var(--page-left) 0%, #1d1d1d 70%, #0c0c0c 100%);
  }
  .page--products {
    background: var(--page);
  }
  .page-title {
    font-family: var(--script);
    font-weight: 400;
    color: var(--ink);
    line-height: 1;
  }
  .page--about .page-title {
    font-size: 64px;
    margin-top: 95px;
  }
  .about-intro,
  .about-offer {
    font-family: var(--sans);
    font-size: 17px;
    line-height: 1.35;
  }
  .about-intro { margin-top: 120px; }
  .about-offer { margin-top: 110px; }

  .page--products .page-title {
    font-size: 78px;
    margin-top: 80px;
  }
  .product-visuals {
    display: flex;
    justify-content: center;
    align-items: center;
    gap: 40px;
    margin-top: 55px;
  }
  .visual-machine {
    width: 190px;
    height: 270px;
    background: linear-gradient(180deg,
      var(--machine-blue) 0%, #5aa6d8 30%,
      var(--machine-green) 55%, #e08a2c 75%, var(--machine-red) 100%);
  }
  .visual-secret-box {
    width: 190px;
    height: 220px;
    background: radial-gradient(circle at 50% 35%, var(--glow) 0%, var(--box-gold) 35%, #6b4d17 60%, var(--page) 78%);
  }
  .product-list {
    display: flex;
    justify-content: center;
    gap: 40px;
    margin-top: 30px;
  }
  .product {
    width: 190px;
  }
  .product-name {
    font-family: var(--script);
    font-weight: 400;
    font-size: 38px;
    line-height: 1.1;
  }
  .product-text {
    font-family: var(--sans);
    font-size: 10px;
    line-height: 1.35;
    margin-top: 10px;
  }
</style>
</head>
<body>
  <main class="spread">
    <section class="page page--about">
      <h2 class="page-title">About us</h2>
      <p class="about-intro">
        We are a young start-up with<br>
        the will to offer our customers<br>
        the widest selection of snacks and more.<br>
        Our range includes not only<br>
        the classic items but also<br>
        new product lines such as<br>
        American or Asian such as manga.
      </p>
      <p class="about-offer">
        We offer a diverse selection of snacks,<br>
        drinks and more in our<br>
        vending machines in Eastern Switzerland
      </p>
    </section>

    <section class="page page--products">
      <h2 class="page-title">Our Products</h2>
      <div class="product-visuals">
        <div class="visual-machine" role="img" aria-label="Photo of vending machine shelves filled with colourful drink bottles"></div>
        <div class="visual-secret-box" role="img" aria-label="Illustration of an open cardboard box with golden sparkling light"></div>
      </div>
      <div class="product-list">
        <article class="product">
          <h3 class="product-name">Snacks</h3>
          <p class="product-text">Delicious snacks, international and innovative products can be found in our snack vending machines.</p>
        </article>
        <article class="product">
          <h3 class="product-name">Secret Packs</h3>
          <p class="product-text">We are the first provider in Switzerland to offer you secret packs in our vending machines.<br><br>The original***</p>
        </article>
      </div>
    </section>
  </main>
</body>
</html>
```